Real State Agency App

We need an app design for a real state agency, we provide mockups for our project that ilustrates very well what we need
our web site is www.brindlevaleestates.com,

Target Market(s)

Tourism

Font styles to use
Other font styles liked:
• attached you will find it

Requirements
Must have
• Colors like the logo

```html
<!DOCTYPE html>
<html lang="en">
<head>
<meta charset="utf-8">
<title>Brindlevale Estates — App Screens</title>
<link href="https://fonts.googleapis.com/css2?family=Ubuntu:wght@400;500&family=Open+Sans:wght@400;600&display=swap" rel="stylesheet">
<style>
:root{
  --stage:#2a3272;
  --blue:#1a9ad6;
  --blue-deep:#1578c2;
  --navy:#0d4a9a;
  --yellow:#fcc93a;
  --ink:#222;
  --muted:#6b6b6b;
  --field:#ececec;
  --white:#fff;
}
*{box-sizing:border-box;margin:0;padding:0}
html,body{width:1200px;height:1200px;overflow:hidden;background:var(--stage)}
body{position:relative;font-family:"Open Sans",sans-serif;color:var(--ink)}
.screen{position:absolute;width:262px;height:463px;background:var(--white);overflow:hidden}
.screen *{position:absolute}
.hero{left:0;top:0;width:262px}
.hero svg{position:static;display:block}
.icon-home,.icon-search{top:14px;width:14px;height:14px}
.icon-home{left:13px}.icon-search{right:13px}
.hero-title{left:0;width:262px;text-align:center;color:var(--white);font-family:"Ubuntu",sans-serif;font-size:15px}
.intro{left:30px;width:202px;text-align:center;font-size:7px;line-height:8.6px;color:var(--muted)}
.field{left:24px;width:213px;height:24px;border:1.5px solid #333;font-size:8px;padding:7px 15px;background:var(--white)}
.btn-yellow{background:var(--yellow);font-size:8px;text-align:center;color:var(--ink)}
.tabs{left:0;bottom:0;width:262px;height:25px;background:var(--yellow)}
.tab{font-family:"Ubuntu",sans-serif;font-size:10.5px;top:7px;color:#222}
.tab.spain{left:32px}.tab.german{left:196px;top:8px}
.tab-active{left:84px;bottom:0;width:95px;height:34px;background:var(--blue);border-radius:5px 5px 0 0;color:#1b3b6a;font-family:"Ubuntu",sans-serif;font-size:10.5px;text-align:center;padding-top:15px}
.brand{left:0;width:262px;top:182px;text-align:center;font-family:"Ubuntu",sans-serif;font-size:19px;color:var(--navy)}
.brand::before{content:"";position:relative;display:inline-block;width:9px;height:9px;border-radius:50%;background:var(--yellow);margin-right:6px;vertical-align:1px}
.tile{width:68px;height:80px;color:var(--white);font-size:7.5px;text-align:center;line-height:9.5px}
.tile svg{left:21px;top:10px}
.tile span{left:0;width:68px;top:40px}
.select{left:25px;width:213px;height:29px;border:1.5px solid #333;font-size:8px;padding:9px 15px;background:var(--white)}
.select::after{content:"";position:absolute;right:12px;top:11px;border:5px solid transparent;border-top:6px solid #333}
.input-soft{left:20px;width:229px;background:var(--field);font-size:6.5px;color:#aaa;padding:9px 13px}
.bar{left:0;top:0;width:262px;height:33px;background:var(--blue);color:var(--white);font-family:"Ubuntu",sans-serif;font-size:10.5px;text-align:center;padding-top:15px}
.result{left:10px;width:233px;height:66px}
.result.active{background:var(--white);box-shadow:0 1px 5px rgba(0,0,0,.18)}
.thumb{left:0;top:0;width:76px;height:66px}
.r-title{left:92px;top:9px;font-size:7px;color:#333}
.r-text{left:92px;top:20px;font-size:5.4px;line-height:7px;color:#777;width:115px}
.r-rate{left:92px;top:43px;font-size:4.5px;color:#777}
.r-rate b{position:relative;display:inline-block;border:1px solid #aaa;padding:1px 3px;font-weight:400;margin-right:3px}
.r-star{left:221px;top:10px;font-size:9px;color:#ccc}
.r-star.on{color:#f5a623}
.body-copy{left:16px;width:230px;text-align:center;font-size:9.6px;line-height:12.2px;color:#333}
.svc{width:99px;height:92px;color:var(--white);font-family:"Ubuntu",sans-serif;font-size:12px;text-align:center;display:flex;align-items:center;justify-content:center;border-radius:3px;line-height:14px}
</style>
</head>
<body>

<!-- Sell your property -->
<section class="screen" style="left:65px;top:93px">
  <div class="hero" role="img" aria-label="Photo of suburban houses tinted blue">
    <svg width="262" height="160" viewBox="0 0 262 160">
      <defs><linearGradient id="g1" x1="0" y1="0" x2="1" y2="1"><stop offset="0" stop-color="#3eb3e6"/><stop offset="1" stop-color="#1a86cc"/></linearGradient></defs>
      <rect width="262" height="160" fill="url(#g1)"/>
      <path d="M0 82 C50 76 120 84 168 122 C190 98 225 70 262 60 L262 160 L0 160Z" fill="#fff"/>
    </svg>
  </div>
  <svg class="icon-home" viewBox="0 0 14 14"><path d="M7 1 L1 7 H3 V13 H6 V9 H8 V13 H11 V7 H13Z" fill="#fff"/></svg>
  <svg class="icon-search" viewBox="0 0 14 14"><circle cx="6" cy="6" r="4.5" stroke="#fff" stroke-width="1.8" fill="none"/><path d="M9.3 9.3 L13 13" stroke="#fff" stroke-width="1.8"/></svg>
  <div class="hero-title" style="top:17px;font-size:8px;font-family:'Open Sans',sans-serif">Sell your Property With us</div>
  <div role="img" aria-label="Portrait of the agent" style="left:92px;top:48px;width:70px;height:70px;border-radius:50%;background:radial-gradient(circle at 50% 40%,#d9a98a,#7a4b33);border:2px solid #fff"></div>
  <p class="intro" style="top:139px">Lorem Ipsum is simply dummy text of the printing and typesetting industry. Lorem Ipsum has been the industry's standard dummy text ever since the 1500s, when an unknown printer took a galley of type</p>
  <div class="field" style="top:194px">Full Name</div>
  <div class="field" style="top:224px">Phone Number</div>
  <div class="field" style="top:256px">Email Address</div>
  <div class="field" style="top:286px">Property Name</div>
  <div class="field" style="top:319px;height:49px">Property Description</div>
  <div class="btn-yellow" style="left:24px;top:376px;width:213px;height:24px;padding-top:7px">Send Now</div>
  <div class="tabs"><span class="tab spain">Spain</span><span class="tab german">Germam</span></div>
  <div class="tab-active">English</div>
</section>

<!-- Home -->
<section class="screen" style="left:342px;top:93px">
  <div class="hero" role="img" aria-label="Photo of a resort pool with palm trees and a woman in a yellow dress">
    <svg width="262" height="170" viewBox="0 0 262 170">
      <defs><linearGradient id="g2" x1="0" y1="0" x2="0" y2="1"><stop offset="0" stop-color="#2f6fa8"/><stop offset=".5" stop-color="#4d7a3e"/><stop offset="1" stop-color="#3ab0e0"/></linearGradient></defs>
      <rect width="262" height="170" fill="url(#g2)"/>
      <path d="M0 120 C60 96 140 104 162 152 C190 115 225 92 262 84 L262 170 L0 170Z" fill="#fff"/>
    </svg>
  </div>
  <div class="brand">Brindlevale</div>
  <div class="field" style="top:227px;height:29px;padding-top:9px">Search Our Properties</div>
  <svg style="left:212px;top:235px" width="13" height="13" viewBox="0 0 14 14"><circle cx="6" cy="6" r="4.5" stroke="#1a9ad6" stroke-width="1.8" fill="none"/><path d="M9.3 9.3 L13 13" stroke="#1a9ad6" stroke-width="1.8"/></svg>
  <div class="tile" style="left:24px;top:272px;background:var(--yellow)">
    <svg width="26" height="26" viewBox="0 0 26 26" fill="none" stroke="#fff" stroke-width="1.3"><path d="M4 13 L13 4 L22 13 M7 11 V22 H19 V11"/><rect x="11" y="15" width="4" height="7"/></svg>
    <span>Our<br>Services</span></div>
  <div class="tile" style="left:97px;top:272px;background:var(--blue)">
    <svg width="26" height="26" viewBox="0 0 26 26" fill="none" stroke="#fff" stroke-width="1.3"><path d="M3 6 H17 L22 11 V23 M10 6 V14 L14 18"/><circle cx="19" cy="19" r="3"/></svg>
    <span>Sell your<br>Property<br>with us</span></div>
  <div class="tile" style="left:169px;top:272px;background:var(--navy)">
    <svg width="26" height="26" viewBox="0 0 26 26" fill="none" stroke="#fff" stroke-width="1.3"><path d="M2 10 L8 6 L13 9 L18 6 L24 10 L18 18 L13 20 L8 18Z M8 12 L13 16 L18 12"/></svg>
    <span>Contact us</span></div>
  <div class="tabs"><span class="tab spain">Spain</span><span class="tab german">Germam</span></div>
  <div class="tab-active">English</div>
</section>

<!-- Search property -->
<section class="screen" style="left:620px;top:93px">
  <div class="hero" role="img" aria-label="Photo of a magnifying glass over a house model, tinted blue">
    <svg width="262" height="160" viewBox="0 0 262 160">
      <defs><linearGradient id="g3" x1="0" y1="0" x2="1" y2="1"><stop offset="0" stop-color="#2a5fb0"/><stop offset="1" stop-color="#1a88cf"/></linearGradient></defs>
      <rect width="262" height="160" fill="url(#g3)"/>
      <path d="M0 120 C70 112 130 118 166 156 C190 120 225 100 262 92 L262 160 L0 160Z" fill="#fff"/>
    </svg>
  </div>
  <svg class="icon-home" viewBox="0 0 14 14"><path d="M7 1 L1 7 H3 V13 H6 V9 H8 V13 H11 V7 H13Z" fill="#fff"/></svg>
  <svg class="icon-search" viewBox="0 0 14 14"><circle cx="6" cy="6" r="4.5" stroke="#fff" stroke-width="1.8" fill="none"/><path d="M9.3 9.3 L13 13" stroke="#fff" stroke-width="1.8"/></svg>
  <div class="hero-title" style="top:57px">Serch Property</div>
  <div class="select" style="top:159px">To Reform</div>
  <div class="select" style="top:196px">Key</div>
  <div class="select" style="top:233px">Type</div>
  <div class="select" style="top:270px">Area</div>
  <div class="btn-yellow" style="left:25px;top:310px;width:213px;height:29px;padding-top:9px">Search Properties</div>
  <div class="tabs"><span class="tab spain">Spain</span><span class="tab german">Germam</span></div>
  <div class="tab-active">English</div>
</section>

<!-- Contact -->
<section class="screen" style="left:898px;top:93px">
  <div class="hero" role="img" aria-label="Photo of hands typing on a keyboard, tinted blue">
    <svg width="262" height="160" viewBox="0 0 262 160">
      <defs><linearGradient id="g4" x1="0" y1="0" x2="1" y2="1"><stop offset="0" stop-color="#3eb3e6"/><stop offset="1" stop-color="#1a8ad0"/></linearGradient></defs>
      <rect width="262" height="160" fill="url(#g4)"/>
      <path d="M0 120 C70 112 130 118 166 156 C190 120 225 100 262 92 L262 160 L0 160Z" fill="#fff"/>
    </svg>
  </div>
  <svg class="icon-home" viewBox="0 0 14 14"><path d="M7 1 L1 7 H3 V13 H6 V9 H8 V13 H11 V7 H13Z" fill="#fff"/></svg>
  <svg class="icon-search" viewBox="0 0 14 14"><circle cx="6" cy="6" r="4.5" stroke="#fff" stroke-width="1.8" fill="none"/><path d="M9.3 9.3 L13 13" stroke="#fff" stroke-width="1.8"/></svg>
  <div class="hero-title" style="top:57px">Contact us</div>
  <div style="left:0;width:268px;top:174px;text-align:center;font-family:'Ubuntu',sans-serif;font-size:13px;color:var(--blue)">Get In Touch</div>
  <div style="left:0;width:268px;top:191px;text-align:center;font-size:6px;color:#444">We are always happy to make valuable new contacts</div>
  <div class="input-soft" style="top:214px;height:26px">Enter your Name</div>
  <div class="input-soft" style="top:245px;height:26px">Enter your Email</div>
  <div class="input-soft" style="top:276px;height:80px">Enter your Email</div>
  <div style="left:20px;top:372px;width:65px;height:22px;background:var(--blue);color:#fff;font-family:'Ubuntu',sans-serif;font-size:10px;text-align:center;padding-top:4px">Send</div>
  <div class="tabs"><span class="tab spain">Spain</span><span class="tab german">Germam</span></div>
  <div class="tab-active">English</div>
</section>

<!-- Search results -->
<section class="screen" style="left:204px;top:581px">
  <div class="bar">Search Results For
    <svg class="icon-home" viewBox="0 0 14 14"><path d="M7 1 L1 7 H3 V13 H6 V9 H8 V13 H11 V7 H13Z" fill="#fff"/></svg>
    <svg class="icon-search" viewBox="0 0 14 14"><circle cx="6" cy="6" r="4.5" stroke="#fff" stroke-width="1.8" fill="none"/><path d="M9.3 9.3 L13 13" stroke="#fff" stroke-width="1.8"/></svg>
  </div>
  <div style="left:0;top:33px;width:262px;height:25px;border-bottom:1px solid #ddd;font-size:7px;padding:9px 11px">Key : Beach, Type: House, Area: Palma</div>
  <div style="left:10px;top:72px;font-family:'Ubuntu',sans-serif;font-size:9.5px;color:#333">Choose Items from below list</div>
  <div style="left:10px;top:85px;font-size:4.5px;color:#777">Finibus Bonorum et Malorum</div>
  <svg style="left:215px;top:77px" width="36" height="12" viewBox="0 0 36 12"><g fill="#ccc"><rect x="0" y="1" width="4" height="4"/><rect x="6" y="1" width="4" height="4"/><rect x="0" y="7" width="4" height="4"/><rect x="6" y="7" width="4" height="4"/></g><g fill="#f5b800"><rect x="21" y="1" width="11" height="2"/><rect x="21" y="5" width="11" height="2"/><rect x="21" y="9" width="11" height="2"/></g></svg>

  <div class="result" style="top:104px"><div class="thumb" role="img" aria-label="Photo of a red brick house" style="background:linear-gradient(#8fb7d9,#b8573d 60%,#5e8a3e)"></div>
    <span class="r-title">Finibus Bonorum et Malorum</span><span class="r-text">Sed ut perspiciatis unde omnis iste natus error sit voluptatem</span><span class="r-rate"><b>4.5</b>/25 Peple Rated</span><span class="r-star">☆</span></div>
  <div class="result active" style="top:175px"><div class="thumb" role="img" aria-label="Photo of a modern house at dusk" style="background:linear-gradient(#2b3f7a,#3d5aa0 55%,#c08a3a)"></div>
    <span class="r-title">Finibus Bonorum et Malorum</span><span class="r-text">Sed ut perspiciatis unde omnis iste natus error sit voluptatem</span><span class="r-rate"><b>4.5</b>/25 Peple Rated</span><span class="r-star on">★</span></div>
  <div class="result" style="top:245px"><div class="thumb" role="img" aria-label="Photo of a lit modern villa" style="background:linear-gradient(#6f8fb8,#4a5a70 55%,#c9a064)"></div>
    <span class="r-title">Finibus Bonorum et Malorum</span><span class="r-text">Sed ut perspiciatis unde omnis iste natus error sit voluptatem</span><span class="r-rate"><b>4.5</b>/25 Peple Rated</span><span class="r-star">☆</span></div>
  <div class="result" style="top:315px"><div class="thumb" role="img" aria-label="Photo of an apartment building at night" style="background:linear-gradient(#2a5db5,#3d7fd0 50%,#c7a46a)"></div>
    <span class="r-title">Finibus Bonorum et Malorum</span><span class="r-text">Sed ut perspiciatis unde omnis iste natus error sit voluptatem</span><span class="r-rate"><b>4.5</b>/25 Peple Rated</span><span class="r-star">☆</span></div>
  <div class="result" style="top:386px"><div class="thumb" role="img" aria-label="Photo of a family house" style="background:linear-gradient(#b9c9d8,#8a8f86 60%,#6d8a4a)"></div>
    <span class="r-title">Finibus Bonorum et Malorum</span><span class="r-text">Sed ut perspiciatis unde omnis iste natus error sit voluptatem</span><span class="r-star on">★</span></div>
  <div class="tabs"><span class="tab spain">Spain</span><span class="tab german">Germam</span></div>
  <div class="tab-active">English</div>
</section>

<!-- Property detail -->
<section class="screen" style="left:482px;top:581px">
  <div class="bar">Villa Brindlevale
    <svg class="icon-home" viewBox="0 0 14 14"><path d="M7 1 L1 7 H3 V13 H6 V9 H8 V13 H11 V7 H13Z" fill="#fff"/></svg>
    <svg class="icon-search" viewBox="0 0 14 14"><circle cx="6" cy="6" r="4.5" stroke="#fff" stroke-width="1.8" fill="none"/><path d="M9.3 9.3 L13 13" stroke="#fff" stroke-width="1.8"/></svg>
  </div>
  <div role="img" aria-label="Photo of a two-storey villa with a porch and garden" style="left:0;top:33px;width:262px;height:154px;background:linear-gradient(#e6eef3,#8d8f80 45%,#5f8a3a 85%)"></div>
  <p class="body-copy" style="top:219px">Lorem Ipsum is simply dummy text of the printing and typesetting industry. Lorem Ipsum has been the industry's standard dummy text ever since the 1500s, when an unknown printer took a galley of type and scrambled it to make a type specimen book. It has survived not only five centuries, but also the leap into electronic typesetting, remaining essentially unchanged. It was popularised in the 1960s with the release of Typeframe sheets containing Lorem Ipsum passages, and more recently with desktop publishing software like Halden PageSetter including versions of Lorem Ipsum.</p>
  <div class="btn-yellow" style="left:34px;top:408px;width:204px;height:34px;border-radius:3px;font-family:'Ubuntu',sans-serif;font-size:12px;padding-top:9px">Send Request Information</div>
</section>

<!-- Services -->
<section class="screen" style="left:759px;top:581px">
  <div class="bar">Our Services
    <svg class="icon-home" viewBox="0 0 14 14"><path d="M7 1 L1 7 H3 V13 H6 V9 H8 V13 H11 V7 H13Z" fill="#fff"/></svg>
    <svg class="icon-search" viewBox="0 0 14 14"><circle cx="6" cy="6" r="4.5" stroke="#fff" stroke-width="1.8" fill="none"/><path d="M9.3 9.3 L13 13" stroke="#fff" stroke-width="1.8"/></svg>
  </div>
  <div style="left:0;top:33px;width:262px;height:204px;background:var(--yellow);box-shadow:0 2px 3px rgba(0,0,0,.15)"></div>
  <p class="body-copy" style="top:60px">Lorem Ipsum is simply dummy text of the printing and typesetting industry. Lorem Ipsum has been the industry's standard dummy text ever since the 1500s, when an unknown printer took a galley of type and scrambled it to make a type specimen book. It has survived not only five centuries, but also the leap into electronic typesetting, remaining essentially unchanged. It was popularised in the 1960s with the release of Typeframe sheets containing Lorem Ipsum passages, and more recently with desktop publishing software like Halden PageSetter including versions of Lorem Ipsum.</p>
  <div class="svc" style="left:26px;top:251px;background:var(--yellow)">Seguros</div>
  <div class="svc" style="left:131px;top:251px;background:var(--blue)">Compra</div>
  <div class="svc" style="left:26px;top:351px;background:var(--blue)">Mantenimientos</div>
  <div class="svc" style="left:131px;top:351px;background:var(--blue)">Obras Y<br>Reformas</div>
</section>

</body>
</html>
```